Billboard Design for Modern Dispensary

Hello!
We need a eye-catching 12' x 24' billboard designed for a very successful, modern cannabis dispensary on the Oregon coast, United States. Because of rules, we cannot have any marijuana leafs or other cannabis related images (flower, joints, smoke, etc). We can use the words "Shop" or "Dispensary" - we cannot use the words "cannabis", "marijuana".

Some ideas we had are 3 words stacked on left or center of billboard - maybe across bottom we have horizontal logo and the following words - “South of bridge in Gullrock Bay”
Another idea is to have a small bubble in bottom/top corner with image of our dog (face only) - with some words around it - like "BONUS Shop Dog" or "Cute Shop Dog" or "Best Shop Dog" or "Friendly Staff"

here's some 3 word examples:
ENJOY
YOUR
TRIP

or

FEEL
GOOD
JUST
AHEAD

or

GOOD
VIBES
ONLY

or

GOOD
TIMES
CHILL
VIBES

I have attached our logo. I have also included a stacked logo version (vertical, not horizontal). the formats are .EPS and .PDF - the logos were created in Affinity Design 2.x.

Our website is coralnook.net if you want to see more images, etc about our dispensary.

Artwork Requirements:
The billboard is 12' tall x 25' wide
The artwork needs to be 1”=1’ @ 300dpi
Please add 6” of bleed all around so your total artwork is 13”x26”
Final deliverable should be .Ai file.

Font styles to use
Sans Serif

Colors
0054AA
0677BA
7BADD7
CADEEF
E8F1F8

Requirements
Nice to have
• See the project description - we included some ideas to consider.
Should not have
• No cannabis images, like flower, cannabis leaves, paraphenlia, cartridges, joints, etc.

```html
<!DOCTYPE html>
<html lang="en">
<head>
<meta charset="utf-8">
<title>Coral Nook Billboard</title>
<link rel="stylesheet" href="https://fonts.googleapis.com/css2?family=Anton&family=Montserrat:wght@300;400&display=swap">
<style>
  :root {
    --page: #f2f2f2;
    --board: #ffffff;
    --ink: #111111;
    --brand-blue: #3a98d4;
    --band-text: #ffffff;
    --wave-tone: #c9c9c9;
  }
  html, body {
    margin: 0;
    padding: 0;
    width: 1199px;
    height: 1200px;
    overflow: hidden;
    background: var(--page);
  }
  .billboard {
    position: absolute;
    left: 50px;
    top: 326px;
    width: 1100px;
    height: 549px;
    background: var(--board);
    overflow: hidden;
  }
  .wave-field {
    position: absolute;
    left: 0;
    top: 0;
    width: 1100px;
    height: 260px;
  }
  .brand {
    position: absolute;
    left: 612px;
    top: 98px;
    display: flex;
    align-items: center;
    gap: 16px;
  }
  .brand-dot {
    width: 104px;
    height: 104px;
    border-radius: 50%;
    background: var(--brand-blue);
  }
  .brand-name {
    font-family: "Montserrat", sans-serif;
    font-weight: 400;
    font-size: 44px;
    letter-spacing: 0.5px;
    color: var(--brand-blue);
    text-transform: uppercase;
    white-space: nowrap;
  }
  .headline {
    position: absolute;
    left: 0;
    right: 0;
    top: 262px;
    margin: 0;
    display: flex;
    justify-content: center;
    align-items: center;
    gap: 22px;
    font-family: "Anton", sans-serif;
    font-weight: 400;
    font-size: 100px;
    line-height: 1;
    color: var(--ink);
    letter-spacing: -1px;
  }
  .headline-divider {
    display: block;
    width: 10px;
    height: 96px;
    background: var(--brand-blue);
  }
  .location-band {
    position: absolute;
    left: 0;
    bottom: 0;
    width: 100%;
    height: 96px;
    background: var(--brand-blue);
    display: flex;
    align-items: center;
    justify-content: center;
  }
  .location-text {
    margin: 0;
    font-family: "Montserrat", sans-serif;
    font-weight: 300;
    font-size: 37px;
    color: var(--band-text);
  }
</style>
</head>
<body>
  <section class="billboard">
    <svg class="wave-field" role="img" aria-label="Decorative flowing line pattern across the top of the board" viewBox="0 0 1100 260" preserveAspectRatio="none">
      <defs>
        <linearGradient id="waveFade" x1="0" y1="0" x2="0" y2="1">
          <stop offset="0" stop-color="#d8d8d8"/>
          <stop offset="1" stop-color="#ffffff"/>
        </linearGradient>
      </defs>
      <path d="M0 0 H1100 V90 C1000 60 930 110 820 80 C700 45 620 10 520 40 C420 70 380 200 280 230 C180 255 80 260 0 250 Z" fill="url(#waveFade)"/>
    </svg>

    <div class="brand">
      <span class="brand-dot"></span>
      <span class="brand-name">Coral Nook</span>
    </div>

    <h1 class="headline">
      <span class="headline-word">SLEEP</span>
      <span class="headline-divider"></span>
      <span class="headline-word">BETTER</span>
      <span class="headline-divider"></span>
      <span class="headline-word">TONIGHT</span>
    </h1>

    <div class="location-band">
      <p class="location-text">South of bridge in Gullrock Bay</p>
    </div>
  </section>
</body>
</html>
```